Brisbane IT support business needs our first website

Hi All,

We are after a new website design for our IT solutions and support business.The business name is Kestrel Harbour Computing Services, or KHCS for short. We provide a range of solutions and services within the IT space.

I would like to utilize the two colours in our business logo I have uploaded.

I understand this is initially for the design only aspect of the site, but I would like to engage the winner to finish coding the website and finalize after also.

Target Market(s)

Other businesses owners and home users.

Industry/Entity Type

Business

Requirements
Must have
• Nice clean and functional design utilizing our business colours from the logo.

```html
<!DOCTYPE html>
<html lang="en">
<head>
<meta charset="utf-8">
<title>Kestrel Harbour Computing Services</title>
<link rel="stylesheet" href="https://fonts.googleapis.com/css2?family=Roboto:wght@300;400;500;700&display=swap">
<style>
:root{
  --blue:#1060b8;
  --blue-dark:#0b3f7a;
  --orange:#f39215;
  --ink:#333840;
  --muted:#8a8f96;
  --line:#e3e5e8;
  --page:#f5f6f7;
  --nav:#2c3440;
  --footer:#eceeef;
  --bottom:#22272e;
}
*{box-sizing:border-box;margin:0;padding:0}
html,body{width:1200px;height:2608px;overflow:hidden}
body{font-family:"Roboto",Arial,sans-serif;color:var(--ink);background:var(--page);font-size:14px}
.wrap{width:1040px;margin:0 auto;position:relative}
.topbar{height:28px;background:#fff;border-bottom:1px solid var(--line);font-size:11px;color:var(--muted)}
.topbar .wrap{display:flex;gap:24px;align-items:center;height:28px}
.header{height:134px;background:#fff}
.header .wrap{display:flex;justify-content:space-between;align-items:center;height:134px}
.brand{display:flex;align-items:center;gap:14px}
.brand-dot{width:64px;height:64px;border-radius:50%;background:var(--blue)}
.brand-name{font-size:40px;font-weight:700;color:var(--blue);letter-spacing:1px}
.questions{text-align:right}
.questions h4{font-size:18px;font-weight:400;color:var(--ink)}
.questions p{color:var(--orange);font-size:16px;margin-top:4px}
.nav{height:36px;background:var(--nav)}
.nav .wrap{display:flex;align-items:center;height:36px}
.nav a{color:#fff;text-decoration:none;font-size:11px;font-weight:500;padding:0 16px;line-height:36px}
.nav a.home{background:var(--orange);width:36px;padding:0;display:flex;align-items:center;justify-content:center;height:36px}
.nav .search{margin-left:auto;width:170px;height:22px;background:#3c4552;color:#aab;font-size:10px;padding:4px 8px;display:flex;justify-content:space-between}
.hero{height:330px;background:linear-gradient(100deg,#0d3f7e 0%,#1d6cc2 45%,#6aa3d8 75%,#2a5f9c 100%);position:relative}
.hero .wrap{padding-top:100px;color:#fff}
.hero h1{font-size:40px;font-weight:400}
.hero p{font-size:13px;margin-top:10px;width:300px;opacity:.9}
.btn{display:inline-block;margin-top:22px;border:1px solid #fff;color:#fff;font-size:11px;padding:8px 18px}
.intro{text-align:center;padding-top:42px}
.intro h2{font-size:26px;font-weight:400;color:var(--blue)}
.intro h2 span{color:var(--orange);font-weight:500}
.intro p{font-size:12px;color:var(--muted);margin-top:8px}
.services{display:flex;gap:24px;margin-top:40px}
.service{flex:1;background:#fff;height:320px;text-align:center;box-shadow:0 1px 3px rgba(0,0,0,.08)}
.service svg.cap{display:block;width:100%;height:130px}
.service h3{font-size:12px;font-weight:700;margin-top:24px}
.service p{font-size:11px;color:var(--muted);margin:14px 28px 0;line-height:1.6}
.more{color:var(--orange);font-size:10px;font-weight:700;margin-top:14px;display:block}
.section-title{text-align:center;font-size:20px;font-weight:400;color:var(--ink);margin-top:58px}
.section-title::after{content:"";display:block;width:30px;height:2px;background:var(--orange);margin:8px auto 0}
.projects{display:flex;gap:28px;margin-top:30px}
.project{flex:1;text-align:center}
.project .photo{height:210px}
.project h3{font-size:12px;font-weight:700;margin-top:18px}
.project p{font-size:11px;color:var(--muted);margin-top:8px}
.load{text-align:center;margin-top:40px;color:var(--orange);font-size:11px;font-weight:700}
.load svg{display:block;margin:6px auto 0}
.tiles{display:flex;justify-content:center;gap:36px;margin-top:26px}
.tile{width:130px;height:130px;background:#fff;box-shadow:0 1px 3px rgba(0,0,0,.08);text-align:center;padding-top:30px}
.tile .ring{width:42px;height:42px;border:2px solid var(--ink);border-radius:50%;margin:0 auto;display:flex;align-items:center;justify-content:center}
.tile span{display:block;font-size:10px;font-weight:700;margin-top:16px}
.core{height:430px;background:var(--blue);margin-top:92px;color:#fff;text-align:center}
.core h2{font-size:20px;font-weight:400;padding-top:56px}
.core h2::after{content:"";display:block;width:30px;height:2px;background:var(--orange);margin:8px auto 0}
.core-items{display:flex;gap:60px;margin-top:64px}
.core-item{flex:1}
.core-item .disc{width:46px;height:46px;background:#fff;border-radius:50%;margin:0 auto;display:flex;align-items:center;justify-content:center}
.core-item h3{font-size:12px;font-weight:700;margin-top:18px}
.core-item p{font-size:11px;line-height:1.7;margin-top:12px;opacity:.9}
.partners{display:flex;justify-content:space-between;align-items:center;height:90px}
.partner{width:150px;height:26px;background:#c9ccd0;border-radius:3px}
.footer{background:var(--footer);height:360px;border-top:1px solid var(--line)}
.footer .wrap{display:flex;gap:40px;padding-top:36px}
.col{flex:1;font-size:11px;color:var(--muted);line-height:1.7}
.col h4{font-size:13px;color:var(--ink);font-weight:700;margin-bottom:14px}
.col .link{color:var(--orange)}
.col .post{margin-bottom:10px}
.bottom{height:82px;background:var(--bottom);color:#8d939b;font-size:10px}
.bottom .wrap{padding-top:20px}
</style>
</head>
<body>
<div class="topbar"><div class="wrap"><span>14 Wharf Lane, Brisbane</span><span>hello@khcs.com.au</span></div></div>
<header class="header"><div class="wrap">
  <div class="brand"><div class="brand-dot"></div><div class="brand-name">KHCS</div></div>
  <div class="questions"><h4>ANY QUESTIONS?</h4><p>+61 7 3180 2460</p></div>
</div></header>
<nav class="nav"><div class="wrap">
  <a class="home" href="#"><svg width="14" height="14" viewBox="0 0 14 14"><path d="M1 7 7 1l6 6h-2v6H8V9H6v4H3V7z" fill="#fff"/></svg></a>
  <a href="#">SERVICES</a><a href="#">CUSTOMER CARE</a><a href="#">ABOUT US</a><a href="#">CLIENTS</a><a href="#">SITEMAP</a><a href="#">FAQ'S</a><a href="#">CONTACT US</a>
  <div class="search"><span>SEARCH</span><span>&#9906;</span></div>
</div></nav>
<section class="hero" role="img" aria-label="Hand touching a glowing digital network over a world map">
  <div class="wrap"><h1>Support &amp; Services</h1><p>Providing support and services to small and medium sized businesses.</p><span class="btn">GET START</span></div>
</section>
<section class="wrap">
  <div class="intro"><h2>Kestrel Harbour <span>Computing</span> Services</h2><p>Brisbane based Information Technology company providing support and services to small and medium sized businesses.</p></div>
  <div class="services">
    <div class="service"><svg class="cap" viewBox="0 0 242 130"><path d="M0 0h242v104Q125 60 0 130z" fill="var(--blue-dark)"/><rect x="107" y="18" width="28" height="40" rx="3" fill="none" stroke="#fff" stroke-width="3"/><circle cx="121" cy="51" r="2" fill="#fff"/></svg><h3>WEB TO WIRELESS</h3><p>Lorem ipsum dolor sit amet etiam dictum adipis nibh sit amet consect.</p><span class="more">READ MORE</span></div>
    <div class="service"><svg class="cap" viewBox="0 0 242 130"><path d="M0 0h242v104Q125 60 0 130z" fill="var(--blue-dark)"/><rect x="101" y="24" width="40" height="28" fill="none" stroke="#fff" stroke-width="3"/><path d="M101 24l20 16 20-16" fill="none" stroke="#fff" stroke-width="3"/></svg><h3>RECOVERY CELL</h3><p>Lorem ipsum dolor sit amet etiam dictum adipis nibh sit amet consect.</p><span class="more">READ MORE</span></div>
    <div class="service"><svg class="cap" viewBox="0 0 242 130"><path d="M0 0h242v104Q125 60 0 130z" fill="var(--blue-dark)"/><path d="M104 36h8v22h-8zM114 36l8-18c5 0 6 4 5 8l-2 8h12c3 0 5 3 4 6l-4 14c-1 3-3 4-6 4h-17z" fill="none" stroke="#fff" stroke-width="3" stroke-linejoin="round"/></svg><h3>TECHNICAL SUPPORT</h3><p>Lorem ipsum dolor sit amet etiam dictum adipis nibh sit amet consect.</p><span class="more">READ MORE</span></div>
    <div class="service"><svg class="cap" viewBox="0 0 242 130"><path d="M0 0h242v104Q125 60 0 130z" fill="var(--blue-dark)"/><rect x="104" y="26" width="30" height="30" rx="3" fill="none" stroke="#fff" stroke-width="3"/><path d="M116 44l20-22 5 5-20 22h-5z" fill="#fff"/></svg><h3>QUALITY POLICY</h3><p>Lorem ipsum dolor sit amet etiam dictum adipis nibh sit amet consect.</p><span class="more">READ MORE</span></div>
  </div>
  <h2 class="section-title">OUR PROJECTS</h2>
  <div class="projects">
    <div class="project"><div class="photo" role="img" aria-label="Business handshake photo" style="background:linear-gradient(135deg,#b9c6d3,#5d7690)"></div><h3>CLIENT SUPPORT</h3><p>We provide a range of services and solutions.</p></div>
    <div class="project"><div class="photo" role="img" aria-label="Glass office tower photo" style="background:linear-gradient(160deg,#9fc2e4,#2f5f93)"></div><h3>BUSINESS STRATEGY</h3><p>We provide a range of services and solutions.</p></div>
    <div class="project"><div class="photo" role="img" aria-label="Hands working with charts and documents photo" style="background:linear-gradient(135deg,#e6e2dc,#8a7f74)"></div><h3>MARKET RANKING</h3><p>We provide a range of services and solutions.</p></div>
  </div>
  <div class="load">LOAD MORE<svg width="12" height="8" viewBox="0 0 12 8"><path d="M0 0h12L6 8z" fill="var(--orange)"/></svg></div>
  <div class="tiles">
    <div class="tile"><div class="ring"><svg width="18" height="18" viewBox="0 0 18 18"><circle cx="9" cy="9" r="4" fill="none" stroke="#333840" stroke-width="2"/></svg></div><span>ABOUT US</span></div>
    <div class="tile"><div class="ring"><svg width="18" height="18" viewBox="0 0 18 18"><path d="M4 8h3v8H4zM8 8l4-6c2 0 2 2 2 3l-1 3h3l-2 8H8z" fill="#333840"/></svg></div><span>FEATURES</span></div>
    <div class="tile"><div class="ring"><svg width="18" height="18" viewBox="0 0 18 18"><path d="M9 2l6 10H3z" fill="#333840"/><rect x="7" y="12" width="4" height="4" fill="#333840"/></svg></div><span>COMPANY</span></div>
    <div class="tile"><div class="ring"><svg width="18" height="18" viewBox="0 0 18 18"><circle cx="9" cy="9" r="6" fill="none" stroke="#333840" stroke-width="2"/><circle cx="9" cy="9" r="2" fill="#333840"/></svg></div><span>DESIGN</span></div>
  </div>
</section>
<section class="core"><div class="wrap">
  <h2>CORE FEATURES</h2>
  <div class="core-items">
    <div class="core-item"><div class="disc"><svg width="18" height="18" viewBox="0 0 18 18"><path d="M4 9l4 4 7-8" fill="none" stroke="var(--blue)" stroke-width="2.5"/></svg></div><h3>CORE VALUES</h3><p>We are a Brisbane based Information Technology company providing support and services to small and medium sized businesses. We provide a range of services and solutions.</p></div>
    <div class="core-item"><div class="disc"><svg width="18" height="18" viewBox="0 0 18 18"><circle cx="9" cy="9" r="6" fill="none" stroke="var(--blue)" stroke-width="2"/><circle cx="9" cy="9" r="2" fill="var(--blue)"/></svg></div><h3>OUR MISSION</h3><p>We are a Brisbane based Information Technology company providing support and services to small and medium sized businesses. We provide a range of services and solutions.</p></div>
    <div class="core-item"><div class="disc"><svg width="18" height="18" viewBox="0 0 18 18"><path d="M1 9q8-8 16 0-8 8-16 0z" fill="none" stroke="var(--blue)" stroke-width="2"/><circle cx="9" cy="9" r="2.5" fill="var(--blue)"/></svg></div><h3>OUR VISION</h3><p>We are a Brisbane based Information Technology company providing support and services to small and medium sized businesses. We provide a range of services and solutions.</p></div>
  </div>
</div></section>
<div class="wrap partners"><div class="partner"></div><div class="partner"></div><div class="partner"></div><div class="partner"></div><div class="partner"></div></div>
<footer class="footer"><div class="wrap">
  <div class="col"><h4>ABOUT US</h4><p>We provide Training, Time Management and Innovation services for small and medium sized businesses. We use cutting edge technology to deliver reliable support, network setup, backup and data recovery.</p></div>
  <div class="col"><h4>Latest Post</h4><div class="post"><span class="link">Network upgrade tips for offices</span><br>Posted on 28 January 2015</div><div class="post"><span class="link">Keeping your data backed up</span><br>Posted on 28 January 2015</div><div class="post"><span class="link">Choosing the right office laptop</span><br>Posted on 28 January 2015</div></div>
  <div class="col"><h4>GET IN TUCH</h4><p>Phone No : +61 7 3180 2460</p><p>Fax No : +61 7 3180 2461</p><p>Email : <span class="link">hello@khcs.com.au</span></p><p>Website : <span class="link">www.khcs.com.au</span></p><p>Address : 14 Wharf Lane, Brisbane QLD</p></div>
  <div class="col"><h4>USEFUL LINK</h4><p class="link">Our Privacy Policy</p><p class="link">Remote Support</p><p class="link">Services</p><p class="link">Customer Support</p><p class="link">Sitemap</p></div>
</div></footer>
<div class="bottom"><div class="wrap">Copyright 2015. All Rights Reserved. | Privacy Policy</div></div>
</body>
</html>
```